Modern 6 page design, business card, and a banner

I need a website design for my CFO service. The service uses proprietary tech, so it needs to be modern. I also need business card and banner design to match the site.
The banner size is 33.75 X 79.25.
I'm open to colors and styles.

Target Market(s)

Startups

Coding

Coded - Design and coding required

Number of Pages Required

5+ page

```html
<!DOCTYPE html>
<html lang="en">
<head>
<meta charset="utf-8">
<title>Tallo — Visual Finance</title>
<link href="https://fonts.googleapis.com/css2?family=Encode+Sans+Condensed:wght@200;300;400&family=Roboto:wght@400;500;700&display=swap" rel="stylesheet">
<style>
:root{
  --ink:#2e2a54;
  --ink-deep:#262247;
  --ink-soft:#3a3566;
  --teal:#52e0c4;
  --teal-dark:#3cc9ae;
  --white:#ffffff;
  --text:#4c4a63;
  --muted:#8e8ba6;
  --light:#f6f6f9;
  --bar:#3d6fc0;
  --line:#dcdce6;
}
*{box-sizing:border-box;margin:0;padding:0}
html,body{width:1200px;height:4124px;overflow:hidden}
body{font-family:"Roboto",sans-serif;background:var(--white);color:var(--text)}
.page{position:relative;width:1200px;height:4124px;overflow:hidden}
.abs{position:absolute}
.display{font-family:"Encode Sans Condensed",sans-serif;font-weight:300}
.btn{position:absolute;display:flex;align-items:center;justify-content:center;background:var(--teal);color:var(--white);font:700 12px "Roboto",sans-serif;letter-spacing:1.2px;border-radius:4px;box-shadow:0 10px 24px rgba(82,224,196,.3)}
.eyebrow{position:absolute;font:500 13px "Roboto",sans-serif}
.rule{position:absolute;width:40px;height:3px;background:var(--teal)}
.para{position:absolute;font-size:12px;line-height:22.5px}

/* nav */
.nav{position:absolute;left:0;top:0;width:1200px;height:75px;background:var(--ink);z-index:5}
.logo{font-family:"Encode Sans Condensed",sans-serif;font-weight:200;color:var(--white)}
.nav .logo{position:absolute;left:30px;top:22px;font-size:28px}
.nav-links{position:absolute;top:31px;left:0;width:100%;font-size:12px;color:#9b98b8}
.nav-links span{position:absolute}
.nav-links .active{color:var(--teal)}
.nav-links .hover{color:var(--white)}

/* hero */
.hero{position:absolute;left:0;top:75px;width:1200px;height:675px;background:linear-gradient(100deg,#39375f 0%,#56527c 45%,#8a86a6 70%,#4a4670 100%)}
.hero-title{position:absolute;left:171px;top:205px;color:var(--white);font-size:80px;line-height:100px;font-weight:200}

/* phone ui */
.phone{position:absolute;background:var(--ink);border-radius:30px;box-shadow:0 24px 50px rgba(20,18,50,.45)}
.screen{position:absolute;background:var(--white);overflow:hidden}
.card-dark{position:absolute;background:var(--ink-soft);border-radius:12px;box-shadow:0 20px 40px rgba(20,18,50,.35)}
.goal{position:absolute;left:16px;right:16px;font-size:8px;color:#333;border-bottom:1px solid #eee;height:40px}
.goal b{display:block;font-weight:500;margin-top:6px}
.goal i{font-style:normal;color:#999;font-size:7px}
.goal em{position:absolute;right:0;top:6px;font-style:normal}
.goal s{position:absolute;right:0;top:22px;width:24px;height:2px;background:#f0a060;text-decoration:none}

/* section 2 */
.photo{position:absolute;border-radius:10px;box-shadow:0 20px 40px rgba(30,28,60,.2)}
.chip{position:absolute;background:var(--teal);color:var(--white);font:700 12px "Roboto",sans-serif;letter-spacing:.8px;display:flex;align-items:center;justify-content:center;border-radius:3px}
.logo-box{position:absolute;background:var(--ink);border-radius:10px;display:flex;align-items:center;justify-content:center;box-shadow:0 24px 50px rgba(20,18,50,.35);z-index:3}

/* how */
.how{position:absolute;left:0;top:1406px;width:1200px;height:787px;background:linear-gradient(180deg,#332f5c,#2b2752)}
.center-text{position:absolute;left:0;width:1200px;text-align:center}
.step-card{position:absolute;left:300px;top:1760px;width:290px;height:180px;background:var(--ink-deep);border-radius:6px}
.step-label{position:absolute;font:500 12px "Roboto",sans-serif;color:#4b4775;transform:translateX(-50%);white-space:nowrap}
.step-icon{position:absolute;width:46px;height:46px;border-radius:50%;border:1.5px solid #4b4775;transform:translate(-50%,-50%)}

/* why */
.why-bg{position:absolute;left:0;top:2930px;width:1200px;height:662px;background:linear-gradient(90deg,#eeeae4 0%,#f7f6f3 40%,#f4f4f6 60%,#e8e9ee 100%)}
.why-card{position:absolute;left:173px;top:2933px;width:854px;height:455px;background:var(--ink);border-radius:18px}
.footer{position:absolute;left:0;top:3592px;width:1200px;height:532px;background:var(--ink)}
</style>
</head>
<body>
<div class="page">

  <!-- Navigation -->
  <header class="nav">
    <div class="logo">Tallo</div>
    <nav class="nav-links">
      <span class="active" style="left:336px">Home</span>
      <span style="left:416px">About</span>
      <span class="hover" style="left:496px">CFO Services</span>
      <span style="left:616px">Visual Finance</span>
      <span style="left:743px">Press</span>
      <span style="left:822px">Contact</span>
    </nav>
    <div class="btn" style="left:1046px;top:16px;width:128px;height:42px">Get The App</div>
  </header>

  <!-- Hero -->
  <section class="hero" role="img" aria-label="Smiling businessman in a suit checking his phone on a city street"></section>
  <div class="abs" style="left:173px;top:173px;color:var(--white);font:500 14px Roboto,sans-serif">Manage Your Finances</div>
  <h1 class="hero-title display">Anytime,<br>Anywhere.</h1>
  <p class="para" style="left:173px;top:436px;width:260px;color:#e6e5f0">Tallo combines hands-on financial planning services with real-time mobile monitoring.</p>
  <div class="btn" style="left:173px;top:534px;width:165px;height:52px">Get The App</div>

  <!-- hero chart card -->
  <div class="card-dark" style="left:690px;top:565px;width:120px;height:195px;background:var(--ink)">
    <div class="screen" style="left:8px;top:12px;width:104px;height:175px;border-radius:4px">
      <div style="font-size:6px;color:#333;padding:8px 6px">‹ GLOBAL SALES &nbsp; CHART</div>
      <div style="font-size:7px;color:var(--bar);padding:0 6px">ALL</div>
      <svg width="104" height="130" viewBox="0 0 104 130">
        <g fill="var(--bar)"><rect x="20" y="8" width="70" height="6"/><rect x="20" y="20" width="42" height="6"/><rect x="20" y="32" width="30" height="6"/><rect x="20" y="44" width="52" height="6"/><rect x="20" y="56" width="58" height="6"/><rect x="20" y="68" width="74" height="6"/><rect x="20" y="80" width="32" height="6"/></g>
        <g font-size="5" fill="#666" font-family="Roboto"><text x="4" y="13">Jan</text><text x="4" y="25">Feb</text><text x="4" y="37">Mar</text><text x="4" y="49">Apr</text><text x="4" y="61">May</text><text x="4" y="73">Jun</text><text x="4" y="85">Jul</text></g>
      </svg>
    </div>
  </div>

  <!-- hero phone -->
  <div class="phone" style="left:802px;top:344px;width:222px;height:446px">
    <div class="abs" style="left:24px;top:34px;font-size:8px;color:var(--white);width:174px;text-align:center;font-weight:500">GOALS</div>
    <div class="screen" style="left:14px;top:56px;width:194px;height:340px;border-radius:4px">
      <div style="margin:8px;height:20px;background:var(--teal);color:#fff;font-size:9px;display:flex;align-items:center;justify-content:center">Add Goal</div>
      <div class="goal" style="top:36px"><b>New client review</b><i>Ana</i><em>64</em><s></s></div>
      <div class="goal" style="top:76px"><b>Expense audit</b><i>Ana</i><em>50</em><s></s></div>
      <div class="goal" style="top:116px"><b>Q2 statements</b><i>Ana</i><em>20</em><s style="background:#ccc;width:10px"></s></div>
      <div class="goal" style="top:156px"><b>Vendor work list</b><i>Leo</i><em>99</em><s style="background:var(--teal)"></s></div>
      <div class="goal" style="top:196px"><b>Rent negotiations</b><i>Leo</i><em>99</em><s style="background:var(--teal)"></s></div>
      <div class="goal" style="top:236px"><b>Review 2018 budget schedule</b><i>Leo</i><em>99</em><s style="background:var(--teal)"></s></div>
      <div class="goal" style="top:276px"><b>Task for Sam</b><i>Mia</i><em>0</em></div>
      <div class="goal" style="top:316px"><b>HR staff reviews</b><i>Sam</i><em>100</em></div>
    </div>
    <div class="abs" style="left:58px;top:414px;font-size:8px;color:var(--teal)">Goals</div>
    <div class="abs" style="left:140px;top:414px;font-size:8px;color:#9b98b8">To Do</div>
  </div>

  <!-- hero login card -->
  <div class="card-dark" style="left:985px;top:450px;width:178px;height:240px;background:var(--ink-soft)">
    <div class="logo" style="position:absolute;left:0;width:178px;text-align:center;top:26px;font-size:28px">Tallo</div>
    <div class="abs" style="left:30px;top:86px;width:120px;height:20px;background:#4a4578;font-size:7px;color:#b4b1d0;display:flex;align-items:center;justify-content:center">Username</div>
    <div class="abs" style="left:30px;top:122px;width:120px;height:20px;background:#4a4578;font-size:7px;color:#b4b1d0;display:flex;align-items:center;justify-content:center">Password</div>
    <div class="abs" style="left:30px;top:160px;width:120px;height:22px;background:var(--teal);font-size:7px;color:#fff;display:flex;align-items:center;justify-content:center">Login</div>
    <div class="abs" style="left:0;width:178px;top:196px;text-align:center;font-size:7px;color:#b4b1d0">Forgot Password?</div>
  </div>

  <!-- hero dashed connectors -->
  <svg class="abs" style="left:640px;top:370px" width="200" height="260" viewBox="0 0 200 260" fill="none" stroke="var(--teal)" stroke-width="1.5" stroke-dasharray="4 4">
    <path d="M160 16 C110 20 90 60 130 90"/>
    <path d="M40 160 C10 200 30 240 60 250"/>
  </svg>

  <!-- Tailored -->
  <div class="photo" style="left:30px;top:818px;width:289px;height:380px;background:linear-gradient(160deg,#c9b9ad,#8f8079 60%,#5d5560)" role="img" aria-label="Woman in glasses working on a laptop"></div>
  <div class="photo" style="left:349px;top:954px;width:210px;height:352px;background:linear-gradient(160deg,#d8d4cf,#a9a19b 55%,#6b6569)" role="img" aria-label="Woman in glasses checking her phone"></div>
  <div class="chip" style="left:230px;top:932px;width:106px;height:36px">Chart</div>
  <div class="chip" style="left:275px;top:1050px;width:135px;height:36px">Add Goal</div>
  <svg class="abs" style="left:280px;top:850px" width="160" height="500" viewBox="0 0 160 500" fill="none" stroke="var(--teal)" stroke-width="1.5" stroke-dasharray="4 4">
    <path d="M10 16 C90 10 140 40 134 110"/>
    <path d="M140 410 C130 450 80 480 20 488"/>
  </svg>
  <div class="logo-box" style="left:109px;top:1229px;width:210px;height:211px"><span class="logo" style="font-size:76px">Tallo</span></div>

  <div class="eyebrow" style="left:675px;top:920px;color:#6c6bb0">A clear financial plan</div>
  <h2 class="abs display" style="left:673px;top:944px;font-size:46px;color:var(--ink)">Tailored to your goals.</h2>
  <div class="rule" style="left:675px;top:1014px"></div>
  <p class="para" style="left:675px;top:1038px;width:350px">Small businesses can visualize their finances, have a plan they trust and monitor progress daily. No more waiting for the latest monthly or quarterly report from your accountant. No more late nights digging through spreadsheets to figure out where you really stand. No more wondering if you’re prepared for the future.</p>
  <p class="para" style="left:675px;top:1173px;width:350px">Tallo delivers a clear financial plan tailored to your goals, an easy mobile dashboard to track progress on a daily basis and all the professional advice and support you need along the way.</p>

  <!-- How it works -->
  <section class="how"></section>
  <div class="center-text" style="top:1516px;font:500 13px Roboto,sans-serif;color:#6c6bb0">5 Easy Steps</div>
  <h2 class="center-text display" style="top:1540px;font-size:46px;color:var(--white)">How Tallo Works</h2>
  <div class="rule" style="left:580px;top:1612px"></div>
  <p class="para" style="left:340px;top:1635px;width:520px;text-align:center;color:#6f6b96">Tallo combines traditional bookkeeping and “outsourced CFO” services with a customizable visual finance mobile app. We provide everything needed to develop a plan, clean and structure your accounting data and launch your visual finance dashboard.</p>

  <div class="step-card">
    <div class="abs" style="left:30px;top:32px;font:500 16px Roboto,sans-serif;color:var(--white)">Step 1. Develop Plan</div>
    <p class="para" style="left:30px;top:78px;width:200px;color:#8e8ba6">We work with you to develop a 3 to 5 year financial plan tailored to your business goals.</p>
  </div>
  <div class="photo" style="left:565px;top:1744px;width:328px;height:210px;border-radius:6px;background:linear-gradient(135deg,#8d8a9a,#5c5870 50%,#3b3856)" role="img" aria-label="Team meeting around a conference table"></div>
  <svg class="abs" style="left:620px;top:1765px" width="36" height="36" viewBox="0 0 36 36"><circle cx="18" cy="18" r="17" fill="var(--ink)" stroke="#fff"/><path d="M13 16a5 5 0 1 1 10 0c0 3-3 4-3 6h-4c0-2-3-3-3-6zM16 25h4" stroke="#fff" fill="none" stroke-width="1.3"/></svg>
  <svg class="abs" style="left:540px;top:1870px" width="52" height="48" viewBox="0 0 52 48"><rect x="1" y="1" width="50" height="46" rx="6" fill="var(--ink)" stroke="#fff"/><path d="M12 36V24M20 36V18M28 36V26M36 36V14" stroke="#fff" stroke-width="3"/></svg>
  <svg class="abs" style="left:862px;top:1734px" width="50" height="50" viewBox="0 0 50 50"><rect x="10" y="2" width="34" height="44" rx="4" fill="var(--ink)" stroke="#fff"/><path d="M17 12h20M17 20h20M17 28h14M17 36h10" stroke="#fff"/></svg>

  <div class="step-label" style="left:308px;top:2001px;color:var(--teal)">1. Develop Plan</div>
  <div class="step-label" style="left:454px;top:2001px">2. Clean Data</div>
  <div class="step-label" style="left:600px;top:2001px;color:#9b98c8">3. Visual Finances</div>
  <div class="step-label" style="left:746px;top:2001px">4. Monitor Daily</div>
  <div class="step-label" style="left:893px;top:2001px">5. Advice Monthly</div>
  <svg class="abs" style="left:330px;top:2053px" width="540" height="6"><line x1="0" y1="3" x2="540" y2="3" stroke="#4b4775" stroke-dasharray="4 5"/></svg>
  <div class="step-icon" style="left:308px;top:2055px;border-color:var(--teal)"><svg width="44" height="44" viewBox="0 0 44 44"><path d="M17 20a5 5 0 1 1 10 0c0 3-3 4-3 6h-4c0-2-3-3-3-6zM20 29h4" stroke="var(--teal)" fill="none" stroke-width="1.3"/></svg></div>
  <div class="step-icon" style="left:454px;top:2055px"><svg width="44" height="44" viewBox="0 0 44 44"><rect x="14" y="15" width="16" height="14" stroke="#4b4775" fill="none"/></svg></div>
  <div class="step-icon" style="left:600px;top:2055px;border-color:#9b98c8"><svg width="44" height="44" viewBox="0 0 44 44"><path d="M15 29V23M20 29V18M25 29V21M30 29V16" stroke="#9b98c8" stroke-width="2"/></svg></div>
  <div class="step-icon" style="left:746px;top:2055px"><svg width="44" height="44" viewBox="0 0 44 44"><circle cx="21" cy="21" r="6" stroke="#4b4775" fill="none"/><path d="M26 26l4 4" stroke="#4b4775"/></svg></div>
  <div class="step-icon" style="left:893px;top:2055px"><svg width="44" height="44" viewBox="0 0 44 44"><path d="M14 16h16v10H20l-4 4v-4h-2z" stroke="#4b4775" fill="none"/></svg></div>

  <!-- Finances in real time -->
  <div class="eyebrow" style="left:173px;top:2363px;color:#6c6bb0">Visualize your</div>
  <h2 class="abs display" style="left:171px;top:2387px;font-size:46px;color:var(--ink)">Finances in real time.</h2>
  <div class="rule" style="left:173px;top:2457px"></div>
  <p class="para" style="left:173px;top:2480px;width:340px">Tallo delivers an easy-to-understand dashboard using our own mobile app, customized for your business and your specific plan. Relying on clean data and mirroring your actual financial statements, Tallo lets you see what a CFO sees and always be confident you’re looking at real numbers.</p>
  <p class="para" style="left:173px;top:2614px;width:340px">Monitor results daily, understand where you stand versus plan and make better decisions with Tallo Mobile.</p>
  <div class="btn" style="left:173px;top:2707px;width:165px;height:53px">Learn More</div>

  <!-- tablet -->
  <div class="card-dark" style="left:930px;top:2298px;width:180px;height:130px;background:var(--ink)">
    <div class="screen" style="left:10px;top:10px;width:160px;height:110px;background:#234a8a;border-radius:3px">
      <div style="font-size:6px;color:#fff;text-align:center;padding-top:6px">GLOBAL SALES</div>
      <div class="abs" style="left:8px;top:20px;width:66px;height:84px;border:1px solid #5f8fd6"><div style="font-size:9px;color:#fff;padding:6px">$190.3M</div><div class="abs" style="left:8px;top:30px;width:12px;height:48px;background:#6fa4ea"></div></div>
      <div class="abs" style="left:86px;top:20px;width:66px;height:84px;border:1px solid #5f8fd6"><div style="font-size:9px;color:#fff;padding:6px">$78.3M</div><div class="abs" style="left:8px;top:30px;width:12px;height:48px;background:#6fa4ea"></div></div>
    </div>
  </div>
  <div class="logo-box" style="left:722px;top:2410px;width:104px;height:60px;background:var(--ink-soft)"><span class="logo" style="font-size:34px">Tallo</span></div>

  <!-- main chart phone -->
  <div class="phone" style="left:804px;top:2373px;width:220px;height:450px;z-index:2">
    <div class="screen" style="left:12px;top:40px;width:196px;height:360px;border-radius:4px">
      <div style="font-size:8px;color:#333;padding:10px 8px">‹ GLOBAL SALES &nbsp;&nbsp; CHART</div>
      <div style="font-size:8px;color:var(--bar);padding:0 8px">ALL</div>
      <svg width="196" height="300" viewBox="0 0 196 300" font-family="Roboto" font-size="7">
        <g fill="#444"><text x="6" y="14">Jan</text><text x="6" y="34">Feb</text><text x="6" y="54">Mar</text><text x="6" y="74">Apr</text><text x="6" y="94">May</text><text x="6" y="114">Jun</text><text x="6" y="134">Jul</text><text x="6" y="154">Aug</text><text x="6" y="174">Sep</text><text x="6" y="194">Oct</text><text x="6" y="214">Nov</text><text x="6" y="234">Dec</text></g>
        <g fill="var(--bar)"><rect x="26" y="8" width="110" height="8"/><rect x="26" y="28" width="58" height="8"/><rect x="26" y="48" width="28" height="8"/><rect x="26" y="68" width="68" height="8"/><rect x="26" y="88" width="72" height="8"/><rect x="26" y="108" width="130" height="8"/><rect x="26" y="128" width="42" height="8"/></g>
        <g fill="#cfd9ec"><rect x="26" y="148" width="130" height="8"/><rect x="26" y="168" width="100" height="8"/><rect x="26" y="188" width="90" height="8"/><rect x="26" y="208" width="60" height="8"/><rect x="26" y="228" width="80" height="8"/></g>
        <g fill="#e24b4b"><rect x="90" y="26" width="2" height="12"/><rect x="58" y="46" width="2" height="12"/><rect x="92" y="66" width="2" height="12"/><rect x="86" y="86" width="2" height="12"/><rect x="110" y="146" width="2" height="12"/><rect x="150" y="186" width="2" height="12"/><rect x="70" y="206" width="2" height="12"/></g>
        <g fill="#444"><text x="140" y="14">53.5</text><text x="88" y="34">18.0</text><text x="98" y="74">21.1</text><text x="102" y="94">22.7</text><text x="160" y="114">39.7</text><text x="72" y="134">13.1</text><text x="26" y="256">0</text><text x="48" y="256">10.0M</text><text x="84" y="256">20.0M</text><text x="120" y="256">30.0M</text><text x="156" y="256">40.0M</text></g>
      </svg>
    </div>
    <div class="abs" style="left:28px;top:420px;font-size:8px;color:#9b98b8">Report</div>
    <div class="abs" style="left:98px;top:420px;font-size:8px;color:var(--teal)">Chart</div>
    <div class="abs" style="left:166px;top:420px;font-size:8px;color:#9b98b8">Note</div>
  </div>

  <!-- report card -->
  <div class="card-dark" style="left:676px;top:2590px;width:130px;height:200px;background:var(--ink)">
    <div class="screen" style="left:8px;top:12px;width:114px;height:176px;border-radius:3px">
      <div style="font-size:6px;color:#333;padding:8px 6px">‹ GLOBAL SALES &nbsp; REPORT</div>
      <svg width="114" height="150" viewBox="0 0 114 150"><g stroke="#e3e3ea"><line x1="4" y1="20" x2="110" y2="20"/><line x1="4" y1="40" x2="110" y2="40"/><line x1="4" y1="60" x2="110" y2="60"/><line x1="4" y1="80" x2="110" y2="80"/><line x1="4" y1="100" x2="110" y2="100"/><line x1="4" y1="120" x2="110" y2="120"/></g><g fill="#aaa"><rect x="6" y="10" width="18" height="3"/><rect x="36" y="10" width="22" height="3"/><rect x="72" y="10" width="18" height="3"/><rect x="6" y="30" width="14" height="3"/><rect x="36" y="30" width="20" height="3"/><rect x="72" y="30" width="14" height="3"/><rect x="6" y="50" width="14" height="3"/><rect x="36" y="50" width="22" height="3"/><rect x="72" y="50" width="16" height="3"/><rect x="6" y="70" width="14" height="3"/><rect x="36" y="70" width="20" height="3"/><rect x="72" y="70" width="16" height="3"/><rect x="6" y="90" width="14" height="3"/><rect x="36" y="90" width="22" height="3"/><rect x="72" y="90" width="14" height="3"/><rect x="6" y="110" width="14" height="3"/><rect x="36" y="110" width="20" height="3"/><rect x="72" y="110" width="16" height="3"/></g></svg>
    </div>
  </div>
  <svg class="abs" style="left:650px;top:2310px" width="300" height="330" viewBox="0 0 300 330" fill="none" stroke="var(--teal)" stroke-width="1.5" stroke-dasharray="4 4">
    <path d="M96 100 C110 20 220 0 290 30"/>
    <path d="M70 160 C20 180 10 250 26 300"/>
  </svg>

  <!-- Why -->
  <div class="why-bg" role="img" aria-label="Desk with calculator, notes, newspaper and laptop, hands holding a phone"></div>
  <div class="why-card"></div>
  <div class="center-text" style="top:3043px;font:500 13px Roboto,sans-serif;color:#6c6bb0">Traditional + Modern</div>
  <h2 class="center-text display" style="top:3066px;font-size:46px;color:var(--white)">Why Tallo Visual Finance?</h2>
  <div class="rule" style="left:580px;top:3138px"></div>
  <p class="para" style="left:355px;top:3162px;width:490px;text-align:center;color:#7a76a2">Small businesses shouldn’t be forced to choose between the strategic value of traditional financial services and the convenience of modern mobile reporting technology. With Tallo, you have access to decades of financial planning experience and a daily view into real finance reports - all delivered through a mobile app you can take with you on the road, in the field, on the shop floor or wherever you need to be.</p>
  <div class="abs" style="left:563px;top:3324px;width:78px;height:150px;background:var(--ink-deep);border-radius:12px;box-shadow:0 18px 40px rgba(0,0,0,.35)">
    <div class="abs" style="left:6px;top:16px;width:66px;height:118px;background:var(--ink-soft);border-radius:3px"></div>
    <div class="abs" style="left:14px;top:96px;width:50px;height:6px;background:var(--teal)"></div>
  </div>

  <!-- Contact + footer -->
  <footer class="footer"></footer>
  <div class="abs display" style="left:305px;top:3690px;font-size:30px;color:var(--white)">Contact us to learn more about Tallo.</div>
  <div class="btn" style="left:730px;top:3686px;width:164px;height:52px">Contact Us</div>
  <div class="abs" style="left:173px;top:3978px;width:72px;height:72px;background:var(--ink-soft);border-radius:10px;display:flex;align-items:center;justify-content:center"><span class="logo" style="font-size:26px">Tallo</span></div>
  <div class="abs" style="left:261px;top:3973px;font-size:11px;color:#7a76a2">© 2019 Tallo. All Rights Reserved.</div>
  <div class="abs" style="left:797px;top:3973px;font-size:11px;color:#7a76a2">Privacy Policy</div>
  <div class="abs" style="left:920px;top:3973px;font-size:11px;color:#7a76a2">Terms &amp; Conditions</div>
</div>
</body>
</html>
```